DL Flyer,A4 letterhead, with compliments slip, and envelopes
For new safety consultancy business
DL Flyer,A4 letterhead, with compliments slip, and envelopes - Consulting
Creative Brief
Yes
New safety consultancy in Australia, focussing on small to medium industrial businesses.
Modern
Unsure - similar to logo maybe?
DL size FLYER TO be one sided glossy to INCLUDE FOLLOWING WORDS:
Occupational Health and Safety is a minefield of laws and regulations for the unprepared employer. Did you know that no matter how small an employer you are, by law you still need a safety management system? Did you know that you need specific procedures in place to prove that your employees, contractors and visitors are safe?
Let Hazardwell implement an OHS strategy that is cost effective and right for you.
Our services not only include OHS advice but also the development of:
- OHS management systems
- Risk assessments
- Safe work method statements
- Checklists, forms and registers
- Training and toolbox talks
Hazardwell is a local business, accredited in auditing Australian Standard 4801 OHS management systems. To arrange a free OHS pulse check of your systems and find out if you meet legislation, call Hazardwell now on 0418 264 907.
info@hazardwellexample.com.au
www.hazardwellexample.com.au
LETTER HEAD TO INCLUDE following company details:
Company name: Hazardwell
Address: PO Box 58, Brindlemoor NSW 2391
Phone: 0418 264 907
Email: info@hazardwellexample.com.au
Web: www.hazardwellexample.com.au

```html
<!DOCTYPE html>
<html lang="en">
<head>
<meta charset="utf-8">
<title>Hazardwell Stationery</title>
<link href="https://fonts.googleapis.com/css2?family=Open+Sans:ital,wght@0,400;0,700;0,800;1,700&display=swap" rel="stylesheet">
<style>
:root{
  --green:#3c9a2c;
  --green-dark:#2a7a1e;
  --orange:#f3941d;
  --yellow:#ffc40f;
  --ink:#333;
  --paper:#fff;
  --bg:#e9e6e1;
  --sky-top:#5fa9d8;
  --sky-bottom:#cfe6f2;
}
*{box-sizing:border-box;margin:0;padding:0}
html,body{width:1200px;height:932px;overflow:hidden}
body{background:var(--bg);font-family:"Open Sans",Arial,sans-serif;color:var(--ink);position:relative}
.sheet{position:absolute;background:var(--paper);box-shadow:0 3px 10px rgba(0,0,0,.25);overflow:hidden}
.brand{display:flex;align-items:center;gap:6px;font-weight:800;color:var(--green)}
.brand .mark{background:var(--orange);display:block}
.brand-sub{font-size:6px;font-weight:700;letter-spacing:2px;color:var(--green);text-transform:uppercase}
.swoosh{position:absolute;left:0;bottom:0;width:100%}
.swoosh svg{display:block;width:100%;height:100%}

.letterhead{top:113px;width:360px;height:455px}
.letterhead.one{left:55px}
.letterhead.two{left:423px}
.letterhead .brand{position:absolute;left:22px;top:22px;font-size:26px}
.letterhead .brand .mark{width:20px;height:20px}
.letterhead .brand-sub{position:absolute;left:48px;top:58px}
.letterhead .swoosh{height:48px}
.letterhead .details{position:absolute;left:22px;bottom:26px;font-size:5.5px;line-height:1.5;color:var(--ink);z-index:2}

.flyer{left:865px;top:113px;width:295px;height:467px}
.flyer .photo{position:absolute;left:0;top:0;width:100%;height:205px;background:linear-gradient(180deg,var(--sky-top),var(--sky-bottom) 70%,#9bb08a)}
.flyer .intro{position:absolute;left:12px;top:14px;width:140px;font-size:6px;line-height:1.45;color:#123}
.flyer .brand{position:absolute;left:12px;top:212px;font-size:16px}
.flyer .brand .mark{width:12px;height:12px}
.flyer .lead{position:absolute;left:12px;top:240px;width:270px;font-size:6.2px;line-height:1.4}
.flyer h3{position:absolute;left:12px;top:268px;width:270px;font-size:10px;font-style:italic;font-weight:700;color:var(--green-dark);line-height:1.25}
.flyer ul{position:absolute;left:12px;top:300px;list-style:none;font-size:10.5px;line-height:1.55}
.flyer li{display:flex;align-items:center;gap:7px}
.flyer li svg{width:12px;height:12px}
.flyer .closing{position:absolute;left:12px;top:386px;width:270px;font-size:5.8px;line-height:1.4}
.flyer .phone{position:absolute;left:12px;top:418px;display:flex;align-items:center;gap:6px;font-size:20px;font-weight:800;color:var(--ink)}
.flyer .phone svg{width:18px;height:18px}
.flyer .web{position:absolute;left:12px;right:12px;bottom:8px;height:14px;background:var(--orange);color:#fff;font-size:7px;font-weight:700;text-align:center;line-height:14px;border-bottom:3px solid var(--green)}

.envelope{left:50px;top:675px;width:585px;height:220px}
.envelope .flap{position:absolute;left:0;top:0;width:100%;height:40px}
.envelope .brand{position:absolute;left:28px;top:62px;font-size:24px}
.envelope .brand .mark{width:18px;height:18px}
.envelope .brand-sub{position:absolute;left:52px;top:96px}
.envelope .swoosh{height:82px}
.envelope .return{position:absolute;left:28px;bottom:18px;color:#fff;font-size:10px;font-weight:700;line-height:1.5;z-index:2}
.envelope .return span{display:block;font-weight:400;font-size:8px}

.card{width:208px;height:125px}
.card.front.a{left:660px;top:605px}
.card.front.b{left:902px;top:605px}
.card.back.a{left:660px;top:750px}
.card.back.b{left:902px;top:750px}
.card.front .brand{position:absolute;left:10px;top:10px;font-size:14px}
.card.front .brand .mark{width:10px;height:10px}
.card.front .person{position:absolute;right:10px;top:34px;text-align:right;font-size:8px;font-weight:700}
.card.front .person span{display:block;font-size:5.5px;font-weight:400}
.card.front .contact{position:absolute;left:10px;top:48px;font-size:5.5px;line-height:1.5}
.card.front .swoosh{height:36px}
.card.front .contact-foot{position:absolute;left:10px;bottom:6px;font-size:5.5px;line-height:1.5;color:#fff;z-index:2}
.card.back{display:flex;align-items:center;justify-content:center;flex-direction:column;gap:30px}
.card.back.a{background:linear-gradient(180deg,var(--yellow),var(--orange))}
.card.back.b{background:linear-gradient(180deg,#5cb83c,var(--green-dark))}
.card.back .brand{color:#fff;font-size:18px}
.card.back .brand .mark{width:12px;height:12px;background:#fff}
.card.back .url{font-size:5.5px;color:#fff}
</style>
</head>
<body>

<!-- Letterhead (A4) -->
<section class="sheet letterhead one">
  <div class="brand"><span class="mark"></span>Hazardwell</div>
  <div class="brand-sub">Safety Consulting</div>
  <div class="details">PO Box 58, Brindlemoor NSW 2391<br>Phone: 0418 264 907 &nbsp; info@hazardwellexample.com.au<br>www.hazardwellexample.com.au</div>
  <div class="swoosh"><svg viewBox="0 0 360 48" preserveAspectRatio="none"><path d="M0 20 C120 40 240 36 360 4 L360 48 L0 48Z" fill="var(--orange)"/><path d="M0 28 C120 46 240 42 360 14 L360 48 L0 48Z" fill="var(--green)"/></svg></div>
</section>

<!-- Compliments slip / second page -->
<section class="sheet letterhead two">
  <div class="brand"><span class="mark"></span>Hazardwell</div>
  <div class="brand-sub">Safety Consulting</div>
  <div class="details">PO Box 58, Brindlemoor NSW 2391<br>Phone: 0418 264 907 &nbsp; info@hazardwellexample.com.au<br>www.hazardwellexample.com.au</div>
  <div class="swoosh"><svg viewBox="0 0 360 48" preserveAspectRatio="none"><path d="M0 20 C120 40 240 36 360 4 L360 48 L0 48Z" fill="var(--orange)"/><path d="M0 28 C120 46 240 42 360 14 L360 48 L0 48Z" fill="var(--green)"/></svg></div>
</section>

<!-- DL Flyer -->
<section class="sheet flyer">
  <div class="photo" role="img" aria-label="Photo of an orange traffic safety cone on a road under a blue sky"></div>
  <p class="intro">Occupational Health and Safety is a minefield of laws and regulations for the unprepared employer. Did you know that no matter how small an employer you are, by law you still need a safety management system? Did you know that you need specific procedures in place to prove that your employees, contractors and visitors are safe?</p>
  <div class="brand"><span class="mark"></span>Hazardwell</div>
  <p class="lead">Let Hazardwell implement an OHS strategy that is cost effective and right for you.</p>
  <h3>Our services not only include OHS advice but also the development of:</h3>
  <ul>
    <li><svg viewBox="0 0 12 12"><path d="M1 6 L4.5 10 L11 1.5" fill="none" stroke="var(--green)" stroke-width="2.4" stroke-linecap="round"/></svg>OHS management systems</li>
    <li><svg viewBox="0 0 12 12"><path d="M1 6 L4.5 10 L11 1.5" fill="none" stroke="var(--green)" stroke-width="2.4" stroke-linecap="round"/></svg>Risk assessments</li>
    <li><svg viewBox="0 0 12 12"><path d="M1 6 L4.5 10 L11 1.5" fill="none" stroke="var(--green)" stroke-width="2.4" stroke-linecap="round"/></svg>Safe work method statements</li>
    <li><svg viewBox="0 0 12 12"><path d="M1 6 L4.5 10 L11 1.5" fill="none" stroke="var(--green)" stroke-width="2.4" stroke-linecap="round"/></svg>Checklists, forms and registers</li>
    <li><svg viewBox="0 0 12 12"><path d="M1 6 L4.5 10 L11 1.5" fill="none" stroke="var(--green)" stroke-width="2.4" stroke-linecap="round"/></svg>Training and toolbox talks</li>
  </ul>
  <p class="closing">Hazardwell is a local business, accredited in auditing Australian Standard 4801 OHS management systems. To arrange a free OHS pulse check of your systems and find out if you meet legislation, call Hazardwell now on 0418 264 907.</p>
  <div class="phone"><svg viewBox="0 0 24 24"><path d="M6.6 10.8a15 15 0 0 0 6.6 6.6l2.2-2.2a1 1 0 0 1 1-.25 11.4 11.4 0 0 0 3.6.6 1 1 0 0 1 1 1V20a1 1 0 0 1-1 1A17 17 0 0 1 3 4a1 1 0 0 1 1-1h3.5a1 1 0 0 1 1 1c0 1.25.2 2.45.6 3.6a1 1 0 0 1-.25 1z" fill="var(--green)"/></svg>0418 264 907</div>
  <div class="web">www.hazardwellexample.com.au</div>
</section>

<!-- DL Envelope -->
<section class="sheet envelope">
  <div class="flap"><svg viewBox="0 0 585 40" preserveAspectRatio="none" width="100%" height="40"><rect width="585" height="40" fill="var(--yellow)"/><path d="M0 0 H585 V12 L292 40 L0 12Z" fill="var(--orange)"/></svg></div>
  <div class="brand"><span class="mark"></span>Hazardwell</div>
  <div class="brand-sub">Safety Consulting</div>
  <div class="return">PO Box 58, Brindlemoor NSW 2391<span>www.hazardwellexample.com.au</span></div>
  <div class="swoosh"><svg viewBox="0 0 585 82" preserveAspectRatio="none"><path d="M0 24 C200 50 400 44 585 0 L585 82 L0 82Z" fill="var(--orange)"/><path d="M0 34 C200 60 400 54 585 12 L585 82 L0 82Z" fill="var(--green)"/></svg></div>
</section>

<!-- Business cards: fronts -->
<section class="sheet card front a">
  <div class="brand"><span class="mark"></span>Hazardwell</div>
  <div class="person">First Name Last<span>Position Title</span></div>
  <div class="contact">PO Box 58<br>Brindlemoor NSW 2391</div>
  <div class="contact-foot">m: 0418 264 907<br>e: mollyfern@hazardwellexample.com.au</div>
  <div class="swoosh"><svg viewBox="0 0 208 36" preserveAspectRatio="none"><path d="M0 8 C80 20 150 16 208 0 L208 36 L0 36Z" fill="var(--orange)"/><path d="M0 13 C80 26 150 22 208 6 L208 36 L0 36Z" fill="var(--green)"/></svg></div>
</section>
<section class="sheet card front b">
  <div class="brand"><span class="mark"></span>Hazardwell</div>
  <div class="person">First Name Last<span>Position Title</span></div>
  <div class="contact">PO Box 58<br>Brindlemoor NSW 2391</div>
  <div class="contact-foot">m: 0418 264 907<br>e: info@hazardwellexample.com.au</div>
  <div class="swoosh"><svg viewBox="0 0 208 36" preserveAspectRatio="none"><path d="M0 8 C80 20 150 16 208 0 L208 36 L0 36Z" fill="var(--orange)"/><path d="M0 13 C80 26 150 22 208 6 L208 36 L0 36Z" fill="var(--green)"/></svg></div>
</section>

<!-- Business cards: backs -->
<section class="sheet card back a">
  <div class="brand"><span class="mark"></span>Hazardwell</div>
  <div class="url">www.hazardwellexample.com.au</div>
</section>
<section class="sheet card back b">
  <div class="brand"><span class="mark"></span>Hazardwell</div>
  <div class="url">www.hazardwellexample.com.au</div>
</section>

</body>
</html>
```